Solace Chiropractic & Acupuncture Business Cards

I need a business card design that feels elevated. I am open to any of the logo designs uploaded. We have two doctors so I'll need to be able to change out the names.

Information:
Marnie Toller D.C., Dipl. Ac. ASA
584 W 12th St, Ste 320
Larkfield, MN 67419
solacegrove.net
620-555-0147
drmarnie@solacegrove.com
Updates

We have designs we like now, we are just trying to choose between top contenders. Thanks for your submissions!

Contact Information for Business Card

noted in description

Requirements
Must have
• ability to edit info if possible
Nice to have
• Please see our website solacegrove.net for our style and colors

```html
<!DOCTYPE html>
<html lang="en">
<head>
<meta charset="utf-8">
<title>Solace Chiropractic &amp; Acupuncture — Business Card</title>
<link rel="stylesheet" href="https://fonts.googleapis.com/css2?family=Marcellus&family=Cormorant+Garamond:wght@500&display=swap">
<style>
  :root {
    --page: #ffffff;
    --mocha: #6d5e51;
    --cream: #e8d9c6;
    --paper: #efebe7;
    --ink: #343b4c;
    --tan: #c9b6a3;
    --tan-dark: #b39c87;
    --photo-light: #e2d6c9;
    --photo-dark: #6f5f51;
  }
  * { margin: 0; padding: 0; box-sizing: border-box; }
  html, body { width: 1200px; height: 1200px; overflow: hidden; background: var(--page); }
  .canvas { position: relative; width: 1200px; height: 1200px; }

  .card-front {
    position: absolute; left: 173px; top: 89px; width: 861px; height: 492px;
    background: var(--mocha);
    display: flex; align-items: center; justify-content: center;
  }
  .front-name {
    font-family: "Marcellus", serif;
    font-size: 64px; letter-spacing: 2px;
    color: var(--cream);
  }

  .card-back {
    position: absolute; left: 168px; top: 615px; width: 866px; height: 502px;
    background: var(--paper);
  }
  .portrait {
    position: absolute; left: 0; top: 0; width: 290px; height: 100%;
    background: linear-gradient(160deg, var(--photo-light) 0%, #b9a593 45%, var(--photo-dark) 100%);
  }
  .divider-strip {
    position: absolute; left: 290px; top: 0; width: 10px; height: 100%;
    background: var(--paper);
    border-left: 3px solid var(--tan);
  }

  .brand {
    position: absolute; left: 404px; top: 34px; width: 336px;
    color: var(--ink); font-family: "Marcellus", serif; text-align: right;
  }
  .brand-name { font-size: 116px; line-height: 1; letter-spacing: -1px; text-align: left; }
  .brand-tagline { font-size: 14px; letter-spacing: 0.3px; margin-top: 6px; }

  .rule { position: absolute; left: 400px; width: 343px; height: 1px; background: var(--tan); }
  .rule-top { top: 202px; }
  .rule-bottom { top: 277px; }

  .doctor {
    position: absolute; left: 400px; top: 224px;
    font-family: "Marcellus", serif; color: var(--ink);
    display: flex; align-items: baseline; gap: 14px;
  }
  .doctor-name { font-size: 27px; letter-spacing: 0.8px; }
  .doctor-creds { font-family: "Cormorant Garamond", serif; font-size: 17px; font-weight: 500; }

  .contact { position: absolute; left: 400px; top: 300px; list-style: none;
    font-family: "Cormorant Garamond", serif; font-weight: 500; font-size: 17px;
    font-variant-numeric: lining-nums;
    color: var(--ink); letter-spacing: 0.8px; }
  .contact li { display: flex; align-items: flex-start; margin-bottom: 17px; line-height: 20px; }
  .contact svg { width: 20px; height: 20px; margin-right: 16px; flex: none;
    fill: none; stroke: var(--tan-dark); stroke-width: 1.3; stroke-linecap: round; stroke-linejoin: round; }
</style>
</head>
<body>
<div class="canvas">
  <section class="card-front">
    <span class="front-name">Solace</span>
  </section>

  <section class="card-back">
    <div class="portrait" role="img" aria-label="Photo of the chiropractor adjusting a patient's back"></div>
    <div class="divider-strip"></div>

    <div class="brand">
      <div class="brand-name">Solace</div>
      <div class="brand-tagline">CHIROPRACTIC &amp; ACUPUNCTURE</div>
    </div>

    <div class="rule rule-top"></div>
    <div class="doctor">
      <span class="doctor-name">Marnie Toller</span>
      <span class="doctor-creds">D.C., Dipl. Ac. ASA</span>
    </div>
    <div class="rule rule-bottom"></div>

    <ul class="contact">
      <li>
        <svg viewBox="0 0 20 20"><path d="M10 18s-6-6-6-10a6 6 0 0 1 12 0c0 4-6 10-6 10z"/><circle cx="10" cy="8" r="2"/></svg>
        <span>584 W 12th St, Ste 320<br>Larkfield, MN 67419</span>
      </li>
      <li>
        <svg viewBox="0 0 20 20"><circle cx="10" cy="10" r="8"/><ellipse cx="10" cy="10" rx="3.5" ry="8"/><path d="M2 10h16"/></svg>
        <span>solacegrove.net</span>
      </li>
      <li>
        <svg viewBox="0 0 20 20"><path d="M4 2.5l3 .5 1.5 4-2 1.5a10 10 0 0 0 5 5l1.5-2 4 1.5.5 3c-1 1-2 1.5-3 1.5C8 17 3 12 2.5 5.5c0-1 .5-2 1.5-3z"/></svg>
        <span>620-555-0147</span>
      </li>
      <li>
        <svg viewBox="0 0 20 20"><rect x="2" y="4" width="16" height="12" rx="1"/><path d="M2.5 5l7.5 6 7.5-6"/></svg>
        <span>drmarnie@solacegrove.com</span>
      </li>
    </ul>
  </section>
</div>
</body>
</html>
```